Velk Method Body Wash & Shampoo

Label design for an Activated charcoal body wash and shampoo for first responders after fires. Product removes soot and smoke smell. Deep cleansing. Red and black tones in label. Product is deep black and bottle transparent. Label is wrapped around bottle and can be with transparent or coloured background. Bottle diameter is 19cm and height is 17cm.

Target Market(s)

Product will be used by Firefighters, first responders, outdoor/nature active and grill enthusiasts.

Industry/Entity Type

Health and hygiene

Colors
EB3D1F
EC4F4E
F09395
F8D3D4
FCEDEE

Requirements
Must have
• Serious design. Design that fits for 250 and 500ml bottles. Place for ingredients and contact info at the back of the bottle..
Nice to have
• Attractive clean design, attached logo. Logo can be on front or back. "medical" or health associations would be good.
Should not have
• Multi color, pictures. Playfulness.

```html
<!DOCTYPE html>
<html lang="en">
<head>
<meta charset="utf-8">
<title>Velk Method Body Wash &amp; Shampoo – Label</title>
<link rel="stylesheet" href="https://fonts.googleapis.com/css2?family=Teko:wght@500;600&family=Open+Sans:ital,wght@0,400;1,400;1,600&display=swap">
<style>
  :root {
    --backdrop: #f1f1f0;
    --label-black: #000000;
    --brand-red: #d7222a;
    --band-red: #8f0e16;
    --text-white: #ffffff;
  }
  * { box-sizing: border-box; margin: 0; padding: 0; }
  html, body {
    width: 1200px;
    height: 905px;
    overflow: hidden;
    background: var(--backdrop);
  }
  .canvas {
    position: relative;
    width: 1200px;
    height: 905px;
    background: var(--backdrop);
  }
  .label {
    position: absolute;
    left: 395px;
    top: 42px;
    width: 410px;
    height: 820px;
    background: var(--label-black);
    border-radius: 7px;
    color: var(--text-white);
    text-align: center;
    overflow: hidden;
  }
  .label__rule {
    position: absolute;
    left: 0;
    width: 100%;
    height: 6px;
    background: var(--brand-red);
  }
  .label__rule--top { top: 15px; }
  .label__rule--bottom { bottom: 15px; }

  .brand {
    position: absolute;
    top: 96px;
    left: 0;
    width: 100%;
    display: flex;
    align-items: center;
    justify-content: center;
    gap: 12px;
  }
  .brand__dot {
    width: 16px;
    height: 16px;
    border-radius: 50%;
    background: var(--brand-red);
  }
  .brand__name {
    font-family: "Teko", sans-serif;
    font-weight: 600;
    font-size: 74px;
    line-height: 1;
    color: var(--brand-red);
    letter-spacing: 1px;
  }

  .product-name {
    position: absolute;
    top: 282px;
    left: 0;
    width: 100%;
    font-family: "Teko", sans-serif;
    font-weight: 600;
    font-size: 50px;
    line-height: 46px;
    letter-spacing: 1.5px;
    color: var(--brand-red);
  }

  .feature-band {
    position: absolute;
    top: 397px;
    left: 0;
    width: 100%;
    height: 52px;
    background: linear-gradient(90deg, var(--label-black) 0%, var(--band-red) 25%, var(--band-red) 75%, var(--label-black) 100%);
    font-family: "Open Sans", sans-serif;
    font-style: italic;
    color: var(--text-white);
  }
  .feature-band__lead {
    display: block;
    padding-top: 6px;
    font-size: 11px;
    line-height: 14px;
  }
  .feature-band__main {
    display: block;
    font-size: 18px;
    line-height: 24px;
    letter-spacing: 0.5px;
  }
  .feature-band__plus {
    font-style: normal;
    font-weight: 600;
    font-size: 24px;
    margin-right: 4px;
  }

  .approval {
    position: absolute;
    top: 563px;
    left: 0;
    width: 100%;
    font-family: "Teko", sans-serif;
    font-weight: 500;
    font-size: 18px;
    letter-spacing: 0.8px;
    line-height: 1;
  }
  .approval__badge {
    position: absolute;
    top: 596px;
    left: 177px;
    width: 56px;
    height: 56px;
    border-radius: 50%;
    background: var(--brand-red);
  }

  .volume {
    position: absolute;
    top: 710px;
    left: 87px;
    width: 236px;
    border-top: 2px solid var(--text-white);
    padding-top: 10px;
    font-family: "Open Sans", sans-serif;
    font-size: 18px;
    line-height: 24px;
  }
  .volume__sep {
    display: inline-block;
    width: 2px;
    height: 22px;
    background: var(--text-white);
    vertical-align: -5px;
    margin: 0 6px;
  }
</style>
</head>
<body>
<main class="canvas">
  <section class="label" aria-label="Velk Method Body Wash and Shampoo front label">
    <div class="label__rule label__rule--top"></div>

    <div class="brand">
      <span class="brand__dot"></span>
      <span class="brand__name">VELK</span>
    </div>

    <h1 class="product-name">BODY WASH<br>&amp; SHAMPOO</h1>

    <div class="feature-band">
      <span class="feature-band__lead">formulated with</span>
      <span class="feature-band__main"><span class="feature-band__plus">+</span>Activated Charcoal</span>
    </div>

    <p class="approval">APPROVED BY:</p>
    <div class="approval__badge" role="img" aria-label="Partner approval badge"></div>

    <p class="volume">17 fl oz<span class="volume__sep"></span>500 mL</p>

    <div class="label__rule label__rule--bottom"></div>
  </section>
</main>
</body>
</html>
```